Velmora Jewellery 25% off pinwheelr like business card

I need a business card designed, the card will be used to send with sold items from the stores.
Theme is black and gold like the logo and name (see pictures)
Must have the following:

Velmora Jewellery logo front and back (use pictures)

www.velmorajewellery-example.com
shops.bazaarvane.com.au/Velmora-Jewellery
info@velmorajewellery-example.com

Like us on pinwheelr for 25% OFF your next purchase!

FREE shipping worldwide!

```html
<!DOCTYPE html>
<html lang="en">
<head>
<meta charset="utf-8">
<title>Velmora Jewellery – Business Card</title>
<link rel="stylesheet" href="https://fonts.googleapis.com/css2?family=Questrial&family=Arimo:wght@400;700&display=swap">
<style>
  :root {
    --ink: #000000;
    --gold: #d6b46e;
    --gold-bright: #f2c968;
    --gold-muted: #8c7446;
    --divider: #c4520e;
  }
  html, body {
    margin: 0;
    padding: 0;
    width: 923px;
    height: 1200px;
    overflow: hidden;
    background: var(--ink);
  }
  .canvas {
    position: relative;
    width: 923px;
    height: 1200px;
    background: var(--ink);
    overflow: hidden;
  }
  .card-side { position: absolute; left: 0; width: 923px; }
  .card-front { top: 0; height: 597px; }
  .card-back { top: 601px; height: 599px; }
  .divider {
    position: absolute;
    left: 0; top: 596px;
    width: 923px; height: 4px;
    background: var(--divider);
  }

  /* Brand mark */
  .brand-ring { position: absolute; }
  .brand-name {
    position: absolute;
    margin: 0;
    font-family: "Questrial", sans-serif;
    font-weight: 400;
    color: var(--gold);
    text-transform: uppercase;
    line-height: 1;
  }
  .front-ring { left: 372px; top: 155px; }
  .front-name {
    left: 0; top: 366px; width: 923px;
    text-align: center;
    font-size: 42px;
    letter-spacing: 8px;
    line-height: 56px;
  }
  .back-ring { left: 142px; top: 655px; }
  .back-name {
    left: 291px; top: 686px;
    font-size: 27px;
    letter-spacing: 5px;
    line-height: 36px;
  }

  /* Contact block */
  .shop-label {
    position: absolute;
    left: 150px; top: 913px; width: 112px;
    text-align: right;
    font-family: "Arimo", sans-serif;
    font-size: 16px;
    color: var(--gold-muted);
  }
  .contact-list {
    position: absolute;
    left: 290px; top: 877px;
    margin: 0; padding: 0;
    list-style: none;
    font-family: "Arimo", sans-serif;
    font-size: 22px;
    line-height: 31px;
    color: var(--gold-bright);
  }

  /* Social offer */
  .social-badge {
    position: absolute;
    left: 200px; top: 1093px;
    width: 60px; height: 60px;
    border-radius: 8px;
    background: var(--gold-muted);
  }
  .offer {
    position: absolute;
    left: 288px; top: 1089px;
    margin: 0;
    font-family: "Arimo", sans-serif;
    color: var(--gold-bright);
  }
  .offer-lead {
    display: block;
    font-size: 29px;
    letter-spacing: 2.6px;
    line-height: 34px;
  }
  .offer-deal {
    display: block;
    font-size: 29px;
    letter-spacing: 1px;
    line-height: 36px;
  }
  .offer-deal strong { font-weight: 700; letter-spacing: 1.5px; }
  .offer-shipping {
    display: block;
    font-size: 10px;
    letter-spacing: 1px;
    line-height: 12px;
  }
</style>
</head>
<body>
<main class="canvas">
  <section class="card-side card-front">
    <svg class="brand-ring front-ring" width="180" height="180" viewBox="0 0 180 180" aria-hidden="true">
      <circle cx="90" cy="90" r="86" fill="none" stroke="var(--gold)" stroke-width="2"/>
    </svg>
    <h1 class="brand-name front-name">Velmora<br>Jewellery</h1>
  </section>

  <div class="divider"></div>

  <section class="card-side card-back"></section>

  <svg class="brand-ring back-ring" width="120" height="120" viewBox="0 0 120 120" aria-hidden="true">
    <circle cx="60" cy="60" r="57" fill="none" stroke="var(--gold)" stroke-width="1.5"/>
  </svg>
  <p class="brand-name back-name">Velmora<br>Jewellery</p>

  <span class="shop-label">bazaarvane</span>
  <ul class="contact-list">
    <li>www.velmorajewellery-example.com</li>
    <li>shops.bazaarvane.com.au/Velmora-Jewellery</li>
    <li>info@velmorajewellery-example.com</li>
  </ul>

  <div class="social-badge" aria-hidden="true"></div>
  <p class="offer">
    <span class="offer-lead">Like us on pinwheelr...</span>
    <span class="offer-deal"><strong>for 25%</strong> off your next purchase!</span>
    <span class="offer-shipping">FREE shipping worldwide!</span>
  </p>
</main>
</body>
</html>
```